Social media design templates

A variety of templates incorporating our logo and colours to use for our postings on different social media platforms. Must be user friendly and meet our brand image. We have attached our logo to view. We would like some of the templates to offer the ability to insert a background image and others to be a template designed around our logo.

We are black and white in colour, and our values speak to our transparency and honesty, so we are looking for clean cut, sharp straight lines, not using any other colours or curved lines.

We are a recruitment company that will be using these templates
- job posting,
- general announcements,
- blog,
- company newsletter,
- updates,
- testimonials and
- top candidate profiles

We would like a gallery of templates to choose from to use separately that all represent our brand.

```html
<!DOCTYPE html>
<html lang="en">
<head>
<meta charset="utf-8">
<title>Stanmore Talent – Social Templates</title>
<link href="https://fonts.googleapis.com/css2?family=Open+Sans:wght@300;400;600&display=swap" rel="stylesheet">
<style>
  :root {
    --ink: #000000;
    --paper: #ffffff;
    --stage: #b0b0b0;
    --caption-dark: #2b2b2b;
    --caption-light: #a8a8a8;
  }
  html, body {
    margin: 0;
    padding: 0;
    width: 1200px;
    height: 818px;
    overflow: hidden;
    background: var(--stage);
    font-family: "Open Sans", sans-serif;
  }
  .gallery { position: relative; width: 1200px; height: 818px; }
  .template {
    position: absolute;
    display: block;
    box-shadow: 8px 10px 16px rgba(0, 0, 0, 0.55);
  }
  .template--portrait-panel { left: 28px;  top: 19px;  width: 374px; height: 374px; }
  .template--diagonal-photo { left: 799px; top: 19px;  width: 374px; height: 374px; }
  .template--slanted-bands  { left: 415px; top: 422px; width: 370px; height: 370px; }
  .brand-name {
    font-family: "Open Sans", sans-serif;
    font-weight: 600;
    letter-spacing: 0.06em;
  }
  .photo-caption {
    font-family: "Open Sans", sans-serif;
    font-weight: 400;
    font-size: 22px;
  }
  .social-label {
    font-family: "Open Sans", sans-serif;
    font-weight: 600;
    font-size: 9px;
    letter-spacing: 0.04em;
  }
</style>
</head>
<body>
<main class="gallery">

  <!-- Template: white content panel -->
  <svg class="template template--portrait-panel" viewBox="0 0 374 374" xmlns="http://www.w3.org/2000/svg">
    <rect class="card-ground" width="374" height="374" fill="var(--ink)"/>
    <polygon class="corner-wedge" points="0,256 0,374 118,374" fill="var(--paper)"/>
    <rect class="content-panel" x="169" y="19" width="185" height="336" fill="var(--paper)"/>
    <g class="brand-lockup" fill="var(--paper)" text-anchor="middle">
      <rect x="44" y="22" width="30" height="30" fill="none" stroke="var(--paper)" stroke-width="1"/>
      <text class="brand-name" x="59" y="66" font-size="10">STANMORE</text>
      <text class="brand-name" x="59" y="78" font-size="7">TALENT</text>
    </g>
    <g class="social-links" fill="var(--ink)">
      <rect x="204" y="333" width="9" height="9"/>
      <text class="social-label" x="216" y="341">LOOP</text>
      <rect x="245" y="333" width="9" height="9"/>
      <text class="social-label" x="257" y="341">LENS</text>
      <rect x="285" y="333" width="9" height="9"/>
      <text class="social-label" x="297" y="341">CHIRP</text>
    </g>
  </svg>

  <!-- Template: framed diagonal background image -->
  <svg class="template template--diagonal-photo" viewBox="0 0 374 374" xmlns="http://www.w3.org/2000/svg">
    <defs>
      <linearGradient id="seedhead-base" x1="0" y1="0" x2="1" y2="1">
        <stop offset="0" stop-color="#3c3c3c"/>
        <stop offset="0.45" stop-color="#8d8d8d"/>
        <stop offset="1" stop-color="#5e5e5e"/>
      </linearGradient>
      <radialGradient id="seedhead-glow" gradientUnits="userSpaceOnUse" cx="170" cy="270" r="150">
        <stop offset="0" stop-color="#e2e2e2" stop-opacity="0.85"/>
        <stop offset="0.5" stop-color="#bdbdbd" stop-opacity="0.45"/>
        <stop offset="1" stop-color="#bdbdbd" stop-opacity="0"/>
      </radialGradient>
    </defs>
    <rect class="card-ground" width="374" height="374" fill="var(--ink)"/>
    <g class="background-photo" role="img" aria-label="Background photo area: close-up of a dandelion seed head in black and white">
      <polygon points="29,87 29,346 344,346" fill="url(#seedhead-base)"/>
      <polygon points="29,87 29,346 344,346" fill="url(#seedhead-glow)"/>
    </g>
    <polyline class="frame-line" points="104,28 346,28 346,346 28,346 28,87"
              fill="none" stroke="var(--paper)" stroke-width="1.2"/>
    <g class="brand-lockup" fill="var(--paper)" text-anchor="middle">
      <rect x="44" y="22" width="30" height="30" fill="none" stroke="var(--paper)" stroke-width="1"/>
      <text class="brand-name" x="59" y="66" font-size="10">STANMORE</text>
      <text class="brand-name" x="59" y="78" font-size="7">TALENT</text>
    </g>
    <g class="photo-caption" fill="var(--caption-dark)">
      <text x="55" y="260">SAMPLE</text>
      <text x="55" y="288">PHOTO</text>
    </g>
    <g class="social-links" fill="var(--paper)" text-anchor="end">
      <rect x="330" y="228" width="9" height="9"/>
      <text class="social-label" x="326" y="236">LOOP</text>
      <rect x="330" y="256" width="9" height="9"/>
      <text class="social-label" x="326" y="264">LENS</text>
      <rect x="330" y="286" width="9" height="9"/>
      <text class="social-label" x="326" y="294">CHIRP</text>
    </g>
  </svg>

  <!-- Template: slanted bands with image -->
  <svg class="template template--slanted-bands" viewBox="0 0 370 370" xmlns="http://www.w3.org/2000/svg">
    <defs>
      <radialGradient id="lion-glow" gradientUnits="userSpaceOnUse" cx="185" cy="175" r="125">
        <stop offset="0" stop-color="#8a8a8a"/>
        <stop offset="0.45" stop-color="#4a4a4a"/>
        <stop offset="1" stop-color="#0c0c0c"/>
      </radialGradient>
    </defs>
    <rect class="card-ground" width="370" height="370" fill="var(--paper)"/>
    <polygon class="top-band" points="77,20 370,20 370,71 46,71" fill="var(--ink)"/>
    <polygon class="background-photo" role="img" aria-label="Background photo area: black and white portrait of a lion in profile on a dark ground"
             points="0,91 318,91 224,275 0,275" fill="url(#lion-glow)"/>
    <g class="photo-caption" fill="var(--caption-light)">
      <text x="54" y="181">SAMPLE</text>
      <text x="54" y="208">PHOTO</text>
    </g>
    <g class="brand-lockup">
      <rect x="0" y="298" width="107" height="55" fill="var(--ink)"/>
      <rect x="9" y="314" width="24" height="24" fill="none" stroke="var(--paper)" stroke-width="1"/>
      <text class="brand-name" x="40" y="325" font-size="8" fill="var(--paper)">STANMORE</text>
      <text class="brand-name" x="40" y="335" font-size="6" fill="var(--paper)">TALENT</text>
    </g>
    <g class="social-links" fill="var(--ink)">
      <rect x="240" y="339" width="9" height="9"/>
      <text class="social-label" x="252" y="347">LOOP</text>
      <rect x="280" y="339" width="9" height="9"/>
      <text class="social-label" x="292" y="347">LENS</text>
      <rect x="318" y="339" width="9" height="9"/>
      <text class="social-label" x="330" y="347">CHIRP</text>
    </g>
  </svg>

</main>
</body>
</html>
```